New Construction company looking for powerful bold logo. people see the logo, leaves an impression

We need a business card for our new company. We provide site work for commercial projects in South Texas. We clear land, excavation, run under ground utilities, concrete work, dirt work etc. We like the black card. I created a webpage www.tarn-vbuilders.com .... As I grow with projects I will put up pictures with video, and intro music. Want it look cool, bold, powerful, and slick looking. Creating 'TVB'....as my logo (possibly or if you have something you want to have fun with). Just have fun!!....thank you!

Dorian Pruett Business Manager Serving South Texas PO Box 4837 Calloway,TX. 78512 Mobile: 361-752-6083 www.tarn-vbuilders.com dorian@tarn-vbuilders.com you can put this anyway you see fit in your design and layout. thank you

Target Market(s)

General Contractors; Home Builders;

Industry/Entity Type

Construction

Contact Information for Business Card

I want the card to be black.

Font styles to use
Other font styles liked:
• Designer choice

Requirements
Must have
• Tarn-V Construction
• Site Work - Utilities/Concrete/Pad/Grading/Excavation (on the back side)
Nice to have
• Maybe TVB as the logo.....or just a symbol that would be TV.....and then construction to tie it togther...

```html
<!DOCTYPE html>
<html lang="en">
<head>
<meta charset="utf-8">
<title>Tarn-V Construction – Business Card</title>
<link rel="stylesheet" href="https://fonts.googleapis.com/css2?family=Raleway:ital,wght@0,400;0,500;0,600;1,400&display=swap">
<style>
  :root {
    --asphalt: #25232e;
    --asphalt-light: #35333f;
    --safety-yellow: #ffc400;
    --ink: #1b1a1f;
    --white: #ffffff;
    --page: #e6e6e6;
  }
  * { box-sizing: border-box; margin: 0; padding: 0; }
  html, body { width: 1200px; height: 900px; overflow: hidden; }
  body {
    background: var(--page);
    font-family: "Raleway", sans-serif;
    display: flex;
    flex-direction: column;
    align-items: center;
    justify-content: center;
    gap: 40px;
  }
  .card {
    position: relative;
    width: 700px;
    height: 400px;
    overflow: hidden;
    background: radial-gradient(ellipse at 60% 40%, var(--asphalt-light), var(--asphalt) 75%);
    box-shadow: 0 6px 18px rgba(0,0,0,.25);
  }
  .card__surface { position: absolute; inset: 0; }
  .card__shapes { position: absolute; inset: 0; }

  /* Front side */
  .services {
    position: absolute;
    left: 36px;
    top: 22px;
    width: 240px;
    list-style: none;
    color: var(--ink);
  }
  .services li {
    font-size: 25px;
    font-weight: 500;
    letter-spacing: .5px;
    line-height: 1;
    padding: 4px 0 4px 14px;
    border-bottom: 2px dotted rgba(27,26,31,.55);
  }
  .service-area {
    position: absolute;
    left: 48px;
    top: 262px;
    color: var(--ink);
    font-size: 19px;
    line-height: 1.3;
    font-style: italic;
    font-weight: 400;
  }
  .brand-mark {
    position: absolute;
    color: var(--safety-yellow);
    font-weight: 600;
    line-height: 1;
  }
  .brand-mark--small { right: 40px; top: 30px; font-size: 56px; letter-spacing: 18px; margin-right: -18px; }
  .contact-head {
    position: absolute;
    right: 36px;
    top: 110px;
    text-align: right;
  }
  .contact-head__name {
    color: var(--safety-yellow);
    font-size: 34px;
    font-weight: 400;
    line-height: 1;
    text-transform: uppercase;
  }
  .contact-head__role {
    color: var(--white);
    font-size: 20px;
    font-weight: 500;
  }
  .contact-list {
    position: absolute;
    right: 30px;
    top: 200px;
    list-style: none;
    text-align: right;
    color: var(--white);
    font-size: 18px;
  }
  .contact-list li {
    display: flex;
    justify-content: flex-end;
    align-items: center;
    gap: 8px;
    height: 26px;
  }
  .contact-icon { width: 20px; height: 20px; flex: none; }

  /* Back side */
  .brand-mark--large {
    left: 0; right: 0; top: 100px;
    text-align: center;
    font-size: 110px;
    letter-spacing: 40px;
    padding-left: 40px;
  }
  .web-address {
    position: absolute;
    left: 0; right: 0; bottom: 52px;
    text-align: center;
    color: var(--white);
    font-size: 34px;
    font-weight: 400;
  }
  .web-address__domain { color: var(--safety-yellow); }
</style>
</head>
<body>

  <section class="card card--front" aria-label="Business card front">
    <div class="card__surface" role="img" aria-label="Dark asphalt texture"></div>
    <svg class="card__shapes" width="700" height="400" viewBox="0 0 700 400" aria-hidden="true">
      <path d="M0 0 H300 Q250 220 320 400 H0 Z" fill="var(--safety-yellow)"/>
      <path d="M312 0 Q262 220 332 400" fill="none" stroke="var(--white)" stroke-width="4"/>
    </svg>

    <ul class="services">
      <li>SITE WORK</li>
      <li>UTILITIES</li>
      <li>CONCRETE</li>
      <li>PAD</li>
      <li>GRADING</li>
      <li>EXCAVATION</li>
    </ul>
    <p class="service-area">Serving South Texas<br>PO Box 4837<br>Calloway,TX. 78512</p>

    <div class="brand-mark brand-mark--small">TVB</div>
    <div class="contact-head">
      <p class="contact-head__name">Dorian Pruett</p>
      <p class="contact-head__role">Business Manager</p>
    </div>
    <ul class="contact-list">
      <li>361-752-6083
        <svg class="contact-icon" viewBox="0 0 20 20" aria-hidden="true"><circle cx="10" cy="10" r="10" fill="var(--safety-yellow)"/><rect x="6.5" y="4" width="7" height="12" rx="1.5" fill="none" stroke="var(--ink)" stroke-width="1.6"/></svg>
      </li>
      <li>www.tarn-vbuilders.com
        <svg class="contact-icon" viewBox="0 0 20 20" aria-hidden="true"><circle cx="10" cy="10" r="10" fill="var(--safety-yellow)"/><g fill="none" stroke="var(--ink)" stroke-width="1.4"><circle cx="10" cy="10" r="5.5"/><ellipse cx="10" cy="10" rx="2.4" ry="5.5"/><path d="M4.5 10h11"/></g></svg>
      </li>
      <li>dorian@tarn-vbuilders.com
        <svg class="contact-icon" viewBox="0 0 20 20" aria-hidden="true"><circle cx="10" cy="10" r="10" fill="var(--safety-yellow)"/><rect x="4.5" y="6" width="11" height="8" fill="var(--ink)"/><path d="M4.5 6l5.5 4.5L15.5 6" fill="none" stroke="var(--safety-yellow)" stroke-width="1.2"/></svg>
      </li>
    </ul>
  </section>

  <section class="card card--back" aria-label="Business card back">
    <div class="card__surface" role="img" aria-label="Dark asphalt texture"></div>
    <div class="brand-mark brand-mark--large">TVB</div>
    <p class="web-address">www.<span class="web-address__domain">tarn-vbuilders</span>.com</p>
  </section>

</body>
</html>
```